The Festival! Poster for an Annual Dance Showcase

We are looking for a dynamic festival/concert style poster for our annual dance showcase featuring at least one image of our dancers and the main information. The main image should be one of the dancers but there can be a collage of the dancers or smaller images around the poster. I have included some reference images but it can vary from them.

Must have this information;
Date - May 22-26
Location - Mabel Corwin Hale Theatre
Tickets - Vondo.bm

Target Market(s)

Parents and people who love dance

Industry/Entity Type

Dance

Font styles to use
Sans Serif

Colors
E54698
E96AAD
F1A4CE
F9D9EA
FCEFF6

Requirements
Must have
• Logo, Date and Location, Picture of Dancer

```html
<!DOCTYPE html>
<html lang="en">
<head>
<meta charset="utf-8">
<title>Annual Dance Showcase</title>
<link href="https://fonts.googleapis.com/css2?family=Great+Vibes&family=Montserrat:wght@400;600;700;800&display=swap" rel="stylesheet">
<style>
  :root {
    --pink-base: #E96AAD;
    --pink-deep: #E54698;
    --pink-ring: #DE55A2;
    --pink-core: #D92E8E;
    --magenta: #E013A8;
    --pink-light: #F1A4CE;
    --blush: #F9D9EA;
    --ticket: #E8DDE2;
    --ink: #111111;
    --white: #FFFFFF;
    --dancer-a: #F08C78;
    --dancer-b: #E9706A;
  }
  * { margin: 0; padding: 0; box-sizing: border-box; }
  html, body { width: 821px; height: 1200px; overflow: hidden; background: #1a1a1a; }
  .poster {
    position: relative;
    width: 821px;
    height: 1200px;
    overflow: hidden;
    background: var(--pink-base);
    font-family: "Montserrat", sans-serif;
  }
  .backdrop { position: absolute; inset: 0; }
  .dancer-photo {
    position: absolute;
    left: 300px;
    top: 70px;
    width: 300px;
    height: 930px;
    border-radius: 150px 150px 120px 120px;
    background: linear-gradient(170deg, var(--dancer-a) 0%, var(--dancer-b) 60%, #D9867A 100%);
    opacity: 0.92;
  }
  .brand {
    position: absolute;
    left: 42px;
    top: 52px;
    display: flex;
    align-items: center;
    gap: 12px;
    color: var(--white);
  }
  .brand-dot { width: 34px; height: 34px; border-radius: 50%; background: var(--white); }
  .brand-name { font-weight: 700; font-size: 36px; line-height: 1; letter-spacing: -0.5px; }
  .brand-sub { font-weight: 700; font-size: 19px; line-height: 1.2; letter-spacing: 0.3px; }
  .date-box {
    position: absolute;
    left: 532px;
    top: 50px;
    width: 228px;
    height: 100px;
    background: var(--magenta);
    color: var(--white);
    font-weight: 800;
    font-size: 70px;
    line-height: 100px;
    text-align: center;
    letter-spacing: -1px;
  }
  .date-month {
    position: absolute;
    left: 522px;
    top: 150px;
    width: 250px;
    text-align: center;
    color: var(--ink);
    font-weight: 600;
    font-size: 104px;
    line-height: 1.05;
  }
  .title-script {
    position: absolute;
    left: 72px;
    top: 380px;
    font-family: "Great Vibes", cursive;
    font-size: 104px;
    color: var(--white);
    line-height: 1;
  }
  .title-main {
    position: absolute;
    left: 62px;
    top: 478px;
    font-weight: 800;
    font-size: 122px;
    color: var(--white);
    line-height: 1;
    letter-spacing: -2px;
  }
  .title-band {
    position: absolute;
    left: 58px;
    top: 602px;
    width: 404px;
    height: 70px;
    background: var(--magenta);
    color: var(--white);
    font-weight: 700;
    font-size: 48px;
    line-height: 70px;
    letter-spacing: 6px;
    text-align: center;
  }
  .ticket {
    position: absolute;
    left: 40px;
    top: 1010px;
    width: 190px;
    height: 108px;
  }
  .ticket-label {
    position: absolute;
    left: 14px;
    top: 54px;
    transform: translate(-50%, -50%) rotate(-90deg);
    transform-origin: center;
    margin-left: 14px;
    font-weight: 700;
    font-size: 15px;
    letter-spacing: 2px;
    color: var(--ink);
  }
  .ticket-site {
    position: absolute;
    left: 62px;
    top: 8px;
    font-weight: 600;
    font-size: 40px;
    line-height: 1.15;
    color: var(--ink);
  }
  .venue {
    position: absolute;
    right: 80px;
    top: 1020px;
    text-align: right;
    color: var(--white);
    font-weight: 700;
    font-size: 30px;
    line-height: 1.3;
  }
  .venue-pin { position: absolute; right: 36px; top: 1020px; }
</style>
</head>
<body>
<main class="poster">
  <svg class="backdrop" width="821" height="1200" viewBox="0 0 821 1200" aria-hidden="true">
    <circle cx="440" cy="560" r="420" fill="var(--pink-deep)" opacity="0.35"/>
    <circle cx="440" cy="560" r="320" fill="var(--pink-ring)" opacity="0.6"/>
    <circle cx="440" cy="560" r="210" fill="var(--pink-core)" opacity="0.8"/>
    <g stroke-linecap="round">
      <line x1="70" y1="90" x2="210" y2="330" stroke="var(--pink-light)" stroke-width="2"/>
      <line x1="170" y1="120" x2="320" y2="390" stroke="var(--magenta)" stroke-width="6"/>
      <line x1="195" y1="185" x2="300" y2="370" stroke="var(--blush)" stroke-width="3"/>
      <line x1="520" y1="600" x2="690" y2="900" stroke="var(--magenta)" stroke-width="6"/>
      <line x1="560" y1="700" x2="700" y2="950" stroke="var(--blush)" stroke-width="2"/>
      <line x1="730" y1="830" x2="730" y2="980" stroke="var(--white)" stroke-width="2"/>
    </g>
  </svg>

  <div class="dancer-photo" role="img" aria-label="Photo of a dancer in a coral sequinned leotard and flowing skirt, leaping with one arm raised"></div>

  <div class="brand">
    <span class="brand-dot"></span>
    <div>
      <div class="brand-name">STRIDE ARTS</div>
      <div class="brand-sub">SCHOOL OF DANCE</div>
    </div>
  </div>

  <div class="date-box">22-26</div>
  <div class="date-month">MAY</div>

  <h1>
    <span class="title-script">Annual</span>
    <span class="title-main">DANCE</span>
    <span class="title-band">SHOWCASE</span>
  </h1>

  <div class="ticket">
    <svg width="190" height="108" viewBox="0 0 190 108" aria-hidden="true">
      <path d="M8 0 H182 A8 8 0 0 0 190 8 V40 A14 14 0 0 0 190 68 V100 A8 8 0 0 0 182 108 H8 A8 8 0 0 0 0 100 V68 A14 14 0 0 0 0 40 V8 A8 8 0 0 0 8 0 Z" fill="var(--ticket)"/>
      <line x1="50" y1="10" x2="50" y2="98" stroke="var(--pink-deep)" stroke-width="2" stroke-dasharray="4 4"/>
    </svg>
    <span class="ticket-label">TICKETS</span>
    <span class="ticket-site">VONDO.<br>BM</span>
  </div>

  <div class="venue">Mabel Corwin Hale<br>Theatre</div>
  <svg class="venue-pin" width="30" height="44" viewBox="0 0 30 44" aria-hidden="true">
    <path d="M15 2 C7 2 2 8 2 15 C2 26 15 41 15 41 C15 41 28 26 28 15 C28 8 23 2 15 2 Z" fill="none" stroke="var(--white)" stroke-width="2.5"/>
    <circle cx="15" cy="15" r="5" fill="none" stroke="var(--white)" stroke-width="2.5"/>
  </svg>
</main>
</body>
</html>
```